bail bonds business

Need a web design for a Bail Bond company. At Larkmoor Bails, we specialize in getting arrested defendants out of jail. Also, I have all the necessary information already uploaded in the files.

Target Market(s)

Arrested defendants and their families who will post bails on their behalf.

Industry/Entity Type

Business

Coding

Coded - Design and coding required

Number of Pages Required

1 page

```html
<!DOCTYPE html>
<html lang="en">
<head>
<meta charset="utf-8">
<title>Larkmoor Bails</title>
<link href="https://fonts.googleapis.com/css2?family=Oswald:wght@400;500;600&family=Open+Sans:wght@400;600;700&display=swap" rel="stylesheet">
<style>
:root{
  --red:#b3141c;
  --red-dark:#8e0d14;
  --ink:#222;
  --text:#666;
  --muted:#999;
  --line:#e2e2e2;
  --dark:#1c1c1c;
  --darker:#121212;
  --white:#fff;
}
*{box-sizing:border-box;margin:0;padding:0}
html,body{width:874px;height:1200px;overflow:hidden;background:var(--white)}
body{font-family:"Open Sans",Arial,sans-serif;color:var(--text);font-size:8px;line-height:1.55}
.wrap{width:680px;margin:0 auto;position:relative}
h1,h2,h3,.nav a,.btn{font-family:"Oswald",Arial,sans-serif;text-transform:uppercase}

.site-header{height:80px}
.site-header .wrap{display:flex;align-items:center;height:80px}
.brand{display:flex;align-items:center;gap:7px;color:var(--red);font-family:"Oswald",sans-serif;font-weight:600;font-size:19px;text-transform:uppercase;letter-spacing:.5px}
.brand-dot{width:22px;height:22px;border-radius:50%;background:var(--red)}
.contact{margin-left:auto;display:flex;gap:34px}
.contact-item{display:flex;gap:7px;align-items:flex-start;font-size:8px;color:var(--ink);font-weight:600;line-height:1.45;text-transform:uppercase}
.contact-item svg{flex:none;margin-top:1px}

.nav{background:var(--red);height:26px}
.nav .wrap{display:flex;height:26px}
.nav a{color:var(--white);text-decoration:none;font-size:8.5px;letter-spacing:.4px;padding:0 17px;display:flex;align-items:center}
.nav a.active{background:var(--darker)}

.hero{position:relative;height:390px;background:linear-gradient(100deg,#3a3a38 0%,#6b6e6c 30%,#2a2a2a 55%,#4d3a33 80%,#261a17 100%)}
.hero-caption{position:absolute;left:466px;top:138px;width:250px;color:var(--white)}
.hero-caption h1{font-size:30px;font-weight:500;letter-spacing:.5px;line-height:1.1}
.hero-caption p{font-size:9.5px;line-height:1.5;margin-top:8px;background:rgba(0,0,0,.35);padding:2px 4px}
.hero-arrow{position:absolute;top:180px;width:20px;height:20px;border-radius:50%;background:rgba(0,0,0,.45);display:flex;align-items:center;justify-content:center}
.hero-arrow.prev{left:92px}.hero-arrow.next{right:92px}
.hero-dots{position:absolute;bottom:12px;left:50%;transform:translateX(-50%);display:flex;gap:5px}
.hero-dots span{width:6px;height:6px;border-radius:50%;background:rgba(255,255,255,.5)}
.hero-dots span.on{background:var(--red)}
.hero-band{height:14px;background:var(--red)}

.features{padding-top:22px}
.features .wrap{display:flex;gap:20px}
.feature{width:213px}
.feature-photo{height:140px}
.feature h2{color:var(--red);font-size:12px;font-weight:500;line-height:1.25;margin:11px 0 6px}
.feature p{font-size:7.5px}
.btn{display:inline-block;background:var(--red);color:var(--white);font-size:8px;padding:4px 10px;margin-top:10px;letter-spacing:.4px}

.media{padding-top:30px}
.media .wrap{display:flex;gap:28px}
.section-title{font-size:13px;font-weight:500;color:var(--ink);padding-bottom:6px;border-bottom:1px solid var(--line);margin-bottom:12px}
.section-title span{color:var(--red)}
.video{width:380px}
.video-body{display:flex;gap:14px}
.video-frame{width:170px;height:120px;flex:none;position:relative;background:linear-gradient(135deg,#2b2b2b,#7d7d7d 55%,#3a3a3a)}
.video-frame .play{position:absolute;left:50%;top:50%;transform:translate(-50%,-50%)}
.video-text p{font-size:7.5px;margin-bottom:8px}
.news{flex:1}
.news-item{padding-bottom:9px;margin-bottom:9px;border-bottom:1px solid var(--line)}
.news-item h3{font-family:"Open Sans",sans-serif;text-transform:none;color:var(--red);font-size:9px;font-weight:700;margin-bottom:4px}
.news-item p{font-size:7.5px}

.get-started{text-align:center;font-family:"Oswald",sans-serif;font-size:11px;color:var(--ink);letter-spacing:.3px;margin-top:30px;padding-bottom:16px}
.get-started strong{font-weight:600}

.site-footer{position:absolute;left:0;right:0;top:1135px;height:65px;background:var(--dark)}
.site-footer .wrap{display:flex;align-items:center;height:40px}
.social{display:flex;gap:5px}
.social span{width:16px;height:16px;border-radius:50%;border:1px solid #777}
.footer-nav{margin-left:auto;display:flex;gap:12px}
.footer-nav a{color:#bbb;font-size:7px;text-decoration:none;text-transform:uppercase}
.to-top{margin-left:18px}
.copyright{text-align:center;color:#777;font-size:7px;border-top:1px solid #2e2e2e;padding-top:7px}
</style>
</head>
<body>

<header class="site-header">
  <div class="wrap">
    <div class="brand"><span class="brand-dot"></span>Larkmoor Bails</div>
    <div class="contact">
      <div class="contact-item">
        <svg width="10" height="13" viewBox="0 0 10 13"><path d="M5 0a5 5 0 0 0-5 5c0 3.7 5 8 5 8s5-4.3 5-8a5 5 0 0 0-5-5zm0 7a2 2 0 1 1 0-4 2 2 0 0 1 0 4z" fill="#b3141c"/></svg>
        <div>Address: 120 Harlow Ave, Suite 2B<br>Brockton, NY 10210</div>
      </div>
      <div class="contact-item">
        <svg width="12" height="12" viewBox="0 0 12 12"><path d="M2.4 0.5 4.3 2.6 3.4 4.3c.8 1.6 2.2 3 3.8 3.8l1.7-.9 2.1 1.9-1.2 2.2C5 11 1 7 .3 1.7z" fill="#b3141c"/></svg>
        <div>Phone: 555-014-2231<br>Fax: 555-014-2290</div>
      </div>
    </div>
  </div>
</header>

<nav class="nav">
  <div class="wrap">
    <a class="active" href="#">Home</a>
    <a href="#">About Us</a>
    <a href="#">What We Offer</a>
    <a href="#">Our Pride Public Service</a>
    <a href="#">Our Service Area</a>
    <a href="#">Contact Us</a>
  </div>
</nav>

<section class="hero" role="img" aria-label="Photo of a person holding keys beside jail cell bars">
  <div class="hero-caption">
    <h1>Larkmoor Bails</h1>
    <p>Bail out your loved ones fast with trusted, discreet support. Call us anytime, day or night.</p>
  </div>
  <span class="hero-arrow prev"><svg width="8" height="10" viewBox="0 0 8 10"><path d="M6 1 2 5l4 4" stroke="#fff" stroke-width="1.6" fill="none"/></svg></span>
  <span class="hero-arrow next"><svg width="8" height="10" viewBox="0 0 8 10"><path d="M2 1l4 4-4 4" stroke="#fff" stroke-width="1.6" fill="none"/></svg></span>
  <div class="hero-dots"><span class="on"></span><span></span><span></span></div>
</section>
<div class="hero-band"></div>

<section class="features">
  <div class="wrap">
    <article class="feature">
      <div class="feature-photo" role="img" aria-label="Photo of hands in handcuffs" style="background:linear-gradient(135deg,#c9b8a6,#7a6a5e 60%,#3b332e)"></div>
      <h2>Your freedom starts with Larkmoor!</h2>
      <p>Being arrested is stressful for you and your family. Our agents move quickly to post your bond, explain every step, and help you get back to work and home.</p>
      <span class="btn">Read More</span>
    </article>
    <article class="feature">
      <div class="feature-photo" role="img" aria-label="Photo of a worried man in a jail cell" style="background:linear-gradient(135deg,#4b4b4b,#8d7f72 55%,#2e2b28)"></div>
      <h2>Larkmoor gets you out. Larkmoor gets you home</h2>
      <p>We answer the phone at any hour and know every local jail. Tell us where your loved one is held and we start the paperwork right away for release.</p>
      <span class="btn">Read More</span>
    </article>
    <article class="feature">
      <div class="feature-photo" role="img" aria-label="Photo of cuffed wrists against a red background" style="background:linear-gradient(135deg,#d9a9a0,#b3141c 55%,#6e0c10)"></div>
      <h2>We guarantee your bail</h2>
      <p>Our fees follow state rules, with clear terms and flexible payment plans. You always know what you pay, and we stay with you until the case is closed.</p>
      <span class="btn">Read More</span>
    </article>
  </div>
</section>

<section class="media">
  <div class="wrap">
    <div class="video">
      <h2 class="section-title"><span>Our</span> Video</h2>
      <div class="video-body">
        <div class="video-frame" role="img" aria-label="Video still of jail cell bars">
          <svg class="play" width="26" height="26" viewBox="0 0 26 26"><circle cx="13" cy="13" r="12" fill="rgba(0,0,0,.55)" stroke="#fff"/><path d="M10 8l8 5-8 5z" fill="#fff"/></svg>
        </div>
        <div class="video-text">
          <p>Watch how the bail process works, from the first call to release. Our team walks you through forms, fees and court dates so nothing catches you off guard.</p>
          <p>We serve families across the region with respect and privacy. Every case is handled by a licensed agent who knows the courts and cares about the result.</p>
        </div>
      </div>
    </div>
    <div class="news">
      <h2 class="section-title"><span>Latest</span> News</h2>
      <div class="news-item">
        <h3>How to post bail on a weekend</h3>
        <p>A quick guide to getting someone released when courts are closed, and what the agent needs from you.</p>
      </div>
      <div class="news-item">
        <h3>What to bring to your bond meeting</h3>
        <p>Simple checklist of papers, IDs and details that help us finish the bond fast.</p>
      </div>
    </div>
  </div>
</section>

<p class="get-started"><strong>GET STARTED HERE:</strong> 120 Harlow Ave, Suite 2B Brockton, NY 10210 Phone: 555-014-2231</p>

<footer class="site-footer">
  <div class="wrap">
    <div class="social"><span></span><span></span><span></span><span></span></div>
    <div class="footer-nav">
      <a href="#">Home</a><a href="#">About Us</a><a href="#">What We Offer</a><a href="#">Our Pride Public Service</a><a href="#">Our Service Area</a><a href="#">Contact Us</a>
    </div>
    <svg class="to-top" width="12" height="12" viewBox="0 0 12 12"><path d="M2 8l4-4 4 4" stroke="#bbb" stroke-width="1.5" fill="none"/></svg>
  </div>
  <p class="copyright">© Copyright 2024 Larkmoor Bails. All rights reserved.</p>
</footer>

</body>
</html>
```